Salon Signage

We need a new company sign designed for the exterior of our salon. I have attached our current logos for an idea. I have also attached a photo of what salon looks like currently.

```html
<!DOCTYPE html>
<html lang="en">
<head>
<meta charset="utf-8">
<title>Glossmere Beauty Salon – Exterior Sign</title>
<link href="https://fonts.googleapis.com/css2?family=Montserrat:wght@500;800&display=swap" rel="stylesheet">
<style>
  :root {
    --backdrop: #7a7a7a;
    --sign-top: #ffffff;
    --sign-bottom: #c9c9c9;
    --ink: #0a0a0a;
    --brand: #9c2389;
    --brand-pink: #d21f86;
    --hair-dark: #3b2420;
    --hair-mid: #6e4a40;
    --white: #ffffff;
  }
  * { margin: 0; padding: 0; box-sizing: border-box; }
  html, body {
    width: 1200px; height: 1200px; overflow: hidden;
    background: var(--backdrop);
    font-family: "Montserrat", sans-serif;
  }
  .sign {
    position: absolute;
    left: 55px; top: 419px;
    width: 1091px; height: 362px;
    background: linear-gradient(180deg, var(--sign-top) 0%, var(--sign-top) 38%, var(--sign-bottom) 100%);
    overflow: hidden;
  }
  .sign__photo {
    position: absolute;
    left: 0; top: 0;
    width: 290px; height: 362px;
    background: radial-gradient(ellipse at 70% 40%, #c9a08d 0%, var(--hair-mid) 35%, var(--hair-dark) 80%);
    z-index: 2;
  }
  .sign__mark {
    position: absolute;
    left: 318px; top: 62px;
    width: 150px; height: 150px;
    border-radius: 50%;
    background: linear-gradient(160deg, var(--brand), var(--brand-pink));
  }
  .sign__name {
    position: absolute;
    left: 482px; top: 38px;
    font-weight: 800;
    font-size: 90px;
    line-height: 1;
    letter-spacing: -1px;
    color: var(--brand);
    white-space: nowrap;
  }
  .sign__tagline {
    position: absolute;
    right: 56px; top: 142px;
    font-weight: 500;
    font-size: 54px;
    line-height: 1;
    letter-spacing: 0.5px;
    color: var(--ink);
    white-space: nowrap;
  }
  .sign__rule {
    position: absolute;
    left: 280px; right: 0; top: 289px;
    height: 4px;
    background: var(--brand);
  }
  .sign__band {
    position: absolute;
    left: 280px; right: 0; bottom: 0;
    height: 66px;
    background: var(--ink);
    display: flex;
    align-items: center;
    padding-left: 35px;
    color: var(--white);
    font-weight: 800;
    font-size: 44px;
    line-height: 1;
  }
  .sign__services { width: 428px; white-space: nowrap; }
  .sign__contact { display: flex; align-items: center; gap: 10px; white-space: nowrap; }
  .sign__phone-icon { width: 38px; height: 38px; }
</style>
</head>
<body>
  <div class="sign">
    <div class="sign__photo" role="img" aria-label="Photo of a woman with long glossy brown hair in profile"></div>
    <div class="sign__mark"></div>
    <div class="sign__name">GLOSSMERE</div>
    <div class="sign__tagline">Beauty Salon</div>
    <div class="sign__rule"></div>
    <div class="sign__band">
      <span class="sign__services">HAIR &amp; BEAUTY</span>
      <span class="sign__contact">
        <svg class="sign__phone-icon" viewBox="0 0 24 24" aria-hidden="true">
          <path fill="#9c2389" d="M6.6 10.8c1.4 2.8 3.8 5.1 6.6 6.6l2.2-2.2c.3-.3.7-.4 1-.2 1.1.4 2.3.6 3.6.6.6 0 1 .4 1 1V20c0 .6-.4 1-1 1C10.6 21 3 13.4 3 4c0-.6.4-1 1-1h3.5c.6 0 1 .4 1 1 0 1.3.2 2.5.6 3.6.1.3 0 .7-.2 1L6.6 10.8z"/>
          <path fill="none" stroke="#9c2389" stroke-width="1.6" stroke-linecap="round" d="M14 3.5a6.5 6.5 0 0 1 6.5 6.5M14 6.8a3.2 3.2 0 0 1 3.2 3.2"/>
        </svg>
        <span class="sign__number">9415 3720</span>
      </span>
    </div>
  </div>
</body>
</html>
```